Timber Ridge Land Services Business Cards

Need to create a business card with the company logo "Timber Ridge Land Services". The business will provide forestry mulching for land clearing and vegetation control, brush and small tree removal, wildlife habitat improvement and trail and property access creation.

```html
<!DOCTYPE html>
<html lang="en">
<head>
<meta charset="utf-8">
<title>Timber Ridge Land Services – Business Cards</title>
<link rel="stylesheet" href="https://fonts.googleapis.com/css2?family=Montserrat:wght@400;500;700;800&display=swap">
<style>
  :root {
    --backdrop: #3a3b3d;
    --forest: #03614f;
    --forest-deep: #0a5b45;
    --leaf: #6cc070;
    --ink: #1d1d1d;
    --paper: #ffffff;
  }
  * { margin: 0; padding: 0; box-sizing: border-box; }
  html, body {
    width: 1200px; height: 1200px; overflow: hidden;
    background: var(--backdrop);
    font-family: "Montserrat", sans-serif;
  }
  .sheet {
    position: relative; width: 1200px; height: 1200px;
    display: flex; flex-direction: column; align-items: center; justify-content: center; gap: 50px;
  }
  .card {
    position: relative; width: 860px; height: 491px;
    border-radius: 34px; overflow: hidden;
    box-shadow: 0 14px 30px rgba(0,0,0,0.45);
  }
  .card-front { background: var(--paper); }
  .card-back { background: var(--forest); display: flex; align-items: center; justify-content: center; }
  .front-wave { position: absolute; inset: 0; width: 100%; height: 100%; }
  .contact-block { position: absolute; left: 62px; top: 200px; }
  .person-name { color: var(--leaf); font-weight: 500; font-size: 44px; letter-spacing: 1px; line-height: 1; }
  .person-role { color: var(--ink); font-weight: 400; font-size: 22px; letter-spacing: 1px; margin-top: 4px; }
  .contact-list { list-style: none; margin-top: 16px; margin-left: 10px; }
  .contact-list li { display: flex; align-items: flex-start; gap: 12px; font-size: 18px; color: var(--ink); line-height: 1.25; margin-bottom: 4px; }
  .contact-list svg { width: 20px; height: 20px; flex: none; margin-top: 2px; fill: var(--leaf); }
  .brand-front {
    position: absolute; right: 80px; top: 150px; width: 330px; text-align: center;
    color: var(--forest-deep); font-weight: 800; font-size: 38px; line-height: 1.08; text-transform: uppercase;
  }
  .brand-back {
    color: var(--paper); font-weight: 800; font-size: 54px; line-height: 1.08; text-transform: uppercase; text-align: center; width: 520px;
  }
  .brand-sub { display: block; font-size: 0.62em; letter-spacing: 2px; margin-top: 6px; }
</style>
</head>
<body>
<main class="sheet">
  <section class="card card-front">
    <svg class="front-wave" viewBox="0 0 860 491" preserveAspectRatio="none" aria-hidden="true">
      <path fill="#6cc070" d="M205,491 C330,360 560,385 705,300 C790,250 815,180 860,160 L860,491 Z"/>
      <path fill="#ffffff" d="M222,491 C345,374 570,398 712,316 C795,268 822,205 860,186 L860,491 Z"/>
      <path fill="#0a5b45" d="M240,491 C360,388 580,410 720,330 C800,284 828,225 860,210 L860,491 Z"/>
    </svg>
    <div class="brand-front">Timber Ridge<span class="brand-sub">Land Services</span></div>
    <div class="contact-block">
      <h1 class="person-name">FULL NAME</h1>
      <p class="person-role">POSITION</p>
      <ul class="contact-list">
        <li><svg viewBox="0 0 24 24"><path d="M6.6 10.8a15 15 0 0 0 6.6 6.6l2.2-2.2a1 1 0 0 1 1-.25 11.4 11.4 0 0 0 3.6.57 1 1 0 0 1 1 1V20a1 1 0 0 1-1 1A17 17 0 0 1 3 4a1 1 0 0 1 1-1h3.5a1 1 0 0 1 1 1c0 1.25.2 2.45.57 3.57a1 1 0 0 1-.25 1z"/></svg>(000) 000 0000</li>
        <li><svg viewBox="0 0 24 24"><path d="M2 5h20v14H2z M2 5l10 8 10-8" fill="none" stroke="#6cc070" stroke-width="2"/></svg>email@company.com</li>
        <li><svg viewBox="0 0 24 24"><g fill="none" stroke="#6cc070" stroke-width="1.8"><circle cx="12" cy="12" r="9.5"/><ellipse cx="12" cy="12" rx="4" ry="9.5"/><path d="M2.5 12h19M4 7h16M4 17h16"/></g></svg>www.company.com</li>
        <li><svg viewBox="0 0 24 24"><path d="M12 2a7 7 0 0 0-7 7c0 5 7 13 7 13s7-8 7-13a7 7 0 0 0-7-7zm0 9.5A2.5 2.5 0 1 1 12 6.5a2.5 2.5 0 0 1 0 5z"/></svg>123 Name Street, 000<br>Your City, 00000-000</li>
      </ul>
    </div>
  </section>

  <section class="card card-back">
    <div class="brand-back">Timber Ridge<span class="brand-sub">Land Services</span></div>
  </section>
</main>
</body>
</html>
```